Business Card Design

​Silver Harbor Rhythms provides personal, friendly service in a fun and high energy environment. We are based in Vermont.

We would like a card that appeals to a wide range of audiences as we do a wide range of events. Please feel free to check out our website silverharborrhythms.com for inspiration.

Target Market(s)

weddings, corporate, birthday parties, colleges

Industry/Entity Type

Business

Contact Information for Business Card

Silver Harbor Rhythms
Providing Entertainment For All Occasions
555 014 2968
silverharborrhythms@mailquill.net
silverharborrhythms.com

```html
<!DOCTYPE html>
<html lang="en">
<head>
<meta charset="utf-8">
<title>Silver Harbor Rhythms — Business Card</title>
<link href="https://fonts.googleapis.com/css2?family=Heebo:wght@300&display=swap" rel="stylesheet">
<style>
  :root {
    --card-bg: #1f2024;
    --band-green: #3b6526;
    --band-red: #bc2026;
    --accent-red: #c0252b;
    --text-light: #ffffff;
  }
  * { margin: 0; padding: 0; box-sizing: border-box; }
  html, body {
    width: 1200px;
    height: 741px;
    overflow: hidden;
    background: var(--card-bg);
  }
  .card {
    position: relative;
    width: 1200px;
    height: 741px;
    background: var(--card-bg);
    font-family: "Heebo", "Helvetica Neue", Arial, sans-serif;
    font-weight: 300;
    color: var(--text-light);
  }
  .brand {
    position: absolute;
    top: 150px;
    left: 0;
    width: 100%;
    display: flex;
    justify-content: center;
    align-items: center;
    gap: 22px;
  }
  .brand-mark {
    width: 26px;
    height: 26px;
    background: var(--accent-red);
  }
  .brand-name {
    font-size: 54px;
    letter-spacing: 2px;
    color: var(--text-light);
  }
  .tagline {
    position: absolute;
    top: 335px;
    left: 0;
    width: 100%;
    text-align: center;
    font-size: 64px;
    letter-spacing: -0.5px;
    white-space: nowrap;
  }
  .tagline .highlight { color: var(--accent-red); }
  .contact-bar {
    position: absolute;
    left: 0;
    top: 549px;
    width: 1200px;
    height: 192px;
    display: flex;
  }
  .contact-item {
    width: 400px;
    height: 100%;
    display: flex;
    flex-direction: column;
    align-items: center;
    padding-top: 12px;
  }
  .contact-item--phone, .contact-item--email { background: var(--band-green); }
  .contact-item--web { background: var(--band-red); border-left: 1px solid #2a2a2a; }
  .contact-icon { width: 60px; height: 60px; }
  .contact-text {
    margin-top: 50px;
    white-space: nowrap;
    line-height: 1;
  }
  .contact-item--phone .contact-text { font-size: 33px; }
  .contact-item--web .contact-text { font-size: 31px; }
  .contact-item--email .contact-text { font-size: 23px; margin-top: 58px; }
</style>
</head>
<body>
<div class="card">
  <div class="brand">
    <span class="brand-mark"></span>
    <span class="brand-name">Silver Harbor Rhythms</span>
  </div>

  <p class="tagline">Providing Entertainment For <span class="highlight">All</span> Occasions</p>

  <div class="contact-bar">
    <div class="contact-item contact-item--phone">
      <svg class="contact-icon" viewBox="0 0 60 60" aria-hidden="true">
        <path d="M6 22 C6 12 54 12 54 22 L54 27 L42 27 L42 21 C36 18 24 18 18 21 L18 27 L6 27 Z" fill="#fff"/>
        <path d="M20 28 L40 28 L50 48 L10 48 Z" fill="#fff"/>
        <circle cx="30" cy="38" r="5" fill="var(--band-green)"/>
      </svg>
      <span class="contact-text">555 014 2968</span>
    </div>
    <div class="contact-item contact-item--web">
      <svg class="contact-icon" viewBox="0 0 60 60" aria-hidden="true" fill="none" stroke="#fff" stroke-width="3">
        <circle cx="30" cy="30" r="23"/>
        <ellipse cx="30" cy="30" rx="10" ry="23"/>
        <line x1="30" y1="7" x2="30" y2="53"/>
        <line x1="7" y1="30" x2="53" y2="30"/>
        <path d="M11 18 H49 M11 42 H49"/>
      </svg>
      <span class="contact-text">silverharborrhythms.com</span>
    </div>
    <div class="contact-item contact-item--email">
      <svg class="contact-icon" viewBox="0 0 60 60" aria-hidden="true">
        <rect x="3" y="14" width="54" height="32" fill="#fff"/>
        <path d="M5 16 L30 34 L55 16" fill="none" stroke="var(--band-green)" stroke-width="2.5"/>
        <path d="M5 44 L24 29 M55 44 L36 29" fill="none" stroke="var(--band-green)" stroke-width="2"/>
      </svg>
      <span class="contact-text">silverharborrhythms@mailquill.net</span>
    </div>
  </div>
</div>
</body>
</html>
```